3D sculpture business needs a flyer

We are looking for a flyer to promote our custom sculpture and jewelry making service. The primary audience are pregnant women and families looking to make sculptures.
The flyers are to be distributed at locations which deal in pregnancy related businesses. Doula, OB offices, baby product stores etc.
The website (in progress) which will be moved to the domain shortly is: http://tinytwinforge.com. Images can be retrieved from here and others can be made available upon request.
The size should be letter (A4) size.
The contact info to be listed should be:
info@TinyTwinForge.com
512.867.4019
Industry/Entity Type
Jewelry
Look and feel
Each slider illustrates characteristics of the customer's brand and the style your logo design should communicate.

```html
<!DOCTYPE html>
<html lang="en">
<head>
<meta charset="utf-8">
<title>TinyTwinForge Flyer</title>
<link rel="stylesheet" href="https://fonts.googleapis.com/css2?family=Questrial&family=Oswald:wght@600;700&family=Crimson+Text:ital@1&family=Open+Sans:wght@400;700&display=swap">
<style>
  :root {
    --brand-blue: #4a78bd;
    --band-blue: #4a79bf;
    --ink: #2b2b2b;
    --paper: #ffffff;
    --swoosh-dark: #3a3a3a;
    --swoosh-light: #b9b9b9;
    --photo-green: #9fd631;
    --gold-light: #e8c27a;
    --gold-deep: #9c6f2a;
  }
  * { margin: 0; padding: 0; box-sizing: border-box; }
  html, body { width: 877px; height: 1200px; overflow: hidden; background: var(--paper); }
  .flyer { position: relative; width: 877px; height: 1200px; background: var(--paper); overflow: hidden; }

  .hero-photo {
    position: absolute; left: 0; top: 0; width: 877px; height: 505px;
    background:
      radial-gradient(ellipse 150px 260px at 560px 330px, #2a2a2a 0%, #2a2a2a 55%, rgba(42,42,42,0) 70%),
      linear-gradient(180deg, #a6dc36 0%, var(--photo-green) 70%, #8fb845 100%);
  }
  .shapes { position: absolute; left: 0; top: 0; width: 877px; height: 1200px; }

  .tagline {
    position: absolute; left: 32px; top: 518px;
    font-family: "Questrial", sans-serif; font-size: 38px; color: var(--ink); letter-spacing: 0.3px;
  }
  .brand-name {
    position: absolute; left: 36px; top: 566px;
    font-family: "Oswald", sans-serif; font-weight: 600; font-size: 50px; color: var(--brand-blue);
    display: flex; align-items: center; gap: 10px;
  }
  .brand-dot { width: 14px; height: 14px; border-radius: 50%; background: var(--brand-blue); }

  .sculpture-photo {
    position: absolute; left: 56px; top: 655px; width: 230px; height: 440px;
    background: radial-gradient(ellipse at 45% 40%, var(--gold-light) 0%, #c9974a 45%, var(--gold-deep) 100%);
    border-radius: 110px 110px 40px 40px;
  }

  .pitch {
    position: absolute; right: 26px; top: 640px; text-align: right;
    font-family: "Oswald", sans-serif; font-weight: 700; font-size: 34px; line-height: 48px; color: var(--brand-blue);
  }
  .process {
    position: absolute; right: 26px; top: 828px; text-align: right;
    font-family: "Crimson Text", serif; font-style: italic; font-size: 21px; line-height: 34px; color: var(--ink);
  }
  .offer {
    position: absolute; right: 26px; top: 893px;
    font-family: "Crimson Text", serif; font-style: italic; font-size: 38px; color: var(--brand-blue);
  }
  .offer-note {
    position: absolute; right: 26px; top: 950px;
    font-family: "Crimson Text", serif; font-style: italic; font-size: 21px; color: var(--ink);
  }

  .contact-call {
    position: absolute; right: 20px; top: 1075px; text-align: right; color: var(--paper);
    font-family: "Open Sans", sans-serif;
  }
  .call-label { font-size: 23px; line-height: 30px; }
  .call-number { font-weight: 700; font-size: 45px; line-height: 52px; letter-spacing: 1px; }
  .call-note { font-weight: 700; font-size: 15px; line-height: 18px; }
  .contact-email {
    position: absolute; left: 20px; top: 1157px; color: var(--paper);
    font-family: "Open Sans", sans-serif; font-size: 21px;
  }
  .contact-email strong { font-weight: 700; }
</style>
</head>
<body>
<main class="flyer">
  <div class="hero-photo" role="img" aria-label="Photo of a pregnant woman in a black tank top with arms raised over her head, standing in a bright green studio hung with black and white baby photos"></div>

  <svg class="shapes" viewBox="0 0 877 1200" aria-hidden="true">
    <path d="M0 470 C180 430 420 445 877 505 L877 520 L0 520 Z" fill="#cfcfcf"/>
    <path d="M0 474 C180 436 420 451 877 510 L877 520 L0 520 Z" fill="var(--paper)"/>
    <path d="M0 1070 C260 1050 560 1030 877 1000 L877 1012 C560 1045 280 1075 0 1092 Z" fill="var(--swoosh-light)"/>
    <path d="M0 1098 C280 1080 580 1052 877 1016 L877 1024 C580 1064 280 1100 0 1118 Z" fill="var(--swoosh-dark)"/>
    <path d="M0 1142 C300 1118 600 1068 877 1018 L877 1200 L0 1200 Z" fill="var(--band-blue)"/>
  </svg>

  <h2 class="tagline">This is the coolest thing ever!</h2>
  <div class="brand-name"><span>TinyTwinForge.com</span><span class="brand-dot"></span></div>

  <div class="sculpture-photo" role="img" aria-label="Photo of a small gold sculpture of a pregnant woman with arms raised over her head"></div>

  <p class="pitch">Using high tech gear,<br>We create full body<br>scans in seconds</p>
  <p class="process">Then, working some magic behind<br>the curtains we give you a</p>
  <p class="offer">Wonderful Sculpture of yourself</p>
  <p class="offer-note">... a TinyTwin of your very own</p>

  <div class="contact-call">
    <p class="call-label">Call Us Today</p>
    <p class="call-number">512.867.4019</p>
    <p class="call-note">(to ask questions or make an appointment)</p>
  </div>
  <p class="contact-email">Email us <strong>info@TinyTwinForge.com</strong></p>
</main>
</body>
</html>
```